Design a helpdesk ticketing platform *

We are launching a helpdesk ticketing platform. Very much like quellbox.com, merrylark.com, pivolta.com, brisktray.com etc. We have a full mid-fidelity prototype built and we want someone to build the full fidelity of the product.

You can view the full mid-fidelity prototype here: https://lnk.vexora.net/Qa8Lpw

The best way moving forward is to just design the following 4 pages

- Main Dashboard https://lnk.vexora.net/81hRtd
- All tickets https://lnk.vexora.net/jwNoEb
- Viewing a ticket https://lnk.vexora.net/Ys4VmK
- Contacts https://lnk.vexora.net/pHeXuo

Target Market(s)

Small business owners

Industry/Entity Type

Saas

Number of Pages Required

4 page

Font styles to use
Serif
Sans Serif

Colors

Designer to choose colors to be used in the design.

Requirements
Must have
• Must follow the prototype exactly. We are not looking for any UX changes. We want the designe xactly as the prototype is. We are only looking for design ideas.
Should not have
• modern, clean. We'd love to see the primary color as yellow, purple, orange, green or blue. You choose which one you think looks best and go with that.

```html
<!DOCTYPE html>
<html lang="en">
<head>
<meta charset="utf-8">
<title>Deskwell – Dashboard</title>
<link href="https://fonts.googleapis.com/css2?family=Mulish:wght@300;400;500;600;700&display=swap" rel="stylesheet">
<style>
  :root {
    --brand: #a48ad8;
    --brand-deep: #7b52c7;
    --brand-dark: #4a2a8c;
    --sidebar: #323644;
    --sidebar-active: #262a35;
    --sidebar-text: #c9cbd3;
    --page: #f4f4f5;
    --card: #ffffff;
    --item: #f6f6f7;
    --line: #e6e6ea;
    --ink: #262626;
    --muted: #8a8a8f;
    --stamp: #ebebef;
  }
  * { box-sizing: border-box; margin: 0; padding: 0; }
  html, body { width: 1200px; height: 1003px; overflow: hidden; }
  body { font-family: "Mulish", sans-serif; background: var(--page); color: var(--ink); position: relative; }

  .sidebar { position: absolute; left: 0; top: 0; width: 277px; height: 1003px; background: var(--sidebar); }
  .brand-bar { height: 83px; background: var(--brand); display: flex; align-items: center; justify-content: space-between; padding: 0 20px 0 54px; }
  .brand-name { color: #fff; font-weight: 700; font-size: 23px; }
  .menu-toggle { width: 36px; height: 40px; }
  .new-ticket { position: absolute; left: 36px; top: 104px; width: 205px; height: 46px; border-radius: 23px;
    background: linear-gradient(180deg, #8a5ed6, var(--brand-deep)); border: 1.5px solid #c5b2ee;
    color: #fff; font-weight: 700; font-size: 19px; display: flex; align-items: center; justify-content: center; gap: 20px; }
  .nav { position: absolute; top: 170px; left: 0; width: 277px; list-style: none; }
  .nav-item { height: 57px; display: flex; align-items: center; padding-left: 67px; position: relative;
    color: var(--sidebar-text); font-size: 15px; font-weight: 500; letter-spacing: .2px; }
  .nav-item.active { background: var(--sidebar-active); color: #fff; }
  .nav-icon { position: absolute; left: 19px; top: 16px; width: 26px; height: 26px; }
  .nav-caret { position: absolute; right: 18px; top: 22px; }

  .topbar { position: absolute; left: 277px; top: 0; width: 923px; height: 83px; background: #fff; border-bottom: 1px solid var(--line); }
  .page-title { position: absolute; left: 32px; top: 28px; font-size: 21px; font-weight: 500; }
  .search { position: absolute; left: 560px; top: 23px; width: 250px; height: 37px; border: 1px solid #d4d4d8; border-radius: 19px;
    padding-left: 17px; font-size: 15px; color: #666; display: flex; align-items: center; }
  .search svg { position: absolute; right: 14px; top: 9px; }
  .user-strip { position: absolute; right: 0; top: 0; width: 71px; height: 83px; background: #e9e9ee; }
  .avatar { position: absolute; left: 828px; top: 16px; }
  .kebab { position: absolute; right: 30px; top: 32px; }

  .greeting { position: absolute; left: 305px; top: 96px; font-size: 27px; font-weight: 300; color: #333; }
  .greeting span { color: var(--brand); font-weight: 400; }

  .stats { position: absolute; left: 305px; top: 164px; display: flex; gap: 19px; }
  .stat { position: relative; width: 129px; height: 151px; }
  .stat svg { position: absolute; inset: 0; }
  .stat-value { position: absolute; top: 40px; width: 100%; text-align: center; font-size: 38px; font-weight: 700; }
  .stat-label { position: absolute; top: 87px; width: 100%; text-align: center; font-size: 15px; color: var(--muted); }
  .stat.primary .stat-label { color: var(--ink); }
  .stat.zero .stat-value { color: #9a9a9f; }

  .activity { position: absolute; left: 305px; top: 342px; width: 867px; height: 633px; background: var(--card); border-radius: 3px; box-shadow: 0 1px 3px rgba(0,0,0,.05); }
  .activity-head { height: 48px; border-bottom: 1px solid var(--line); padding: 13px 0 0 16px; font-size: 19px; font-weight: 500; }
  .day-tag { position: absolute; left: -10px; height: 27px; padding: 0 20px 0 25px; background: var(--brand); color: #fff;
    font-size: 17px; font-weight: 500; line-height: 27px; border-radius: 0 14px 14px 0; }
  .day-tag::before { content: ""; position: absolute; left: 0; top: 27px; width: 10px; height: 16px; background: var(--brand-dark); border-radius: 0 0 0 6px; }
  .entry { position: absolute; left: 28px; width: 812px; height: 84px; background: var(--item); border: 1px solid var(--line); border-radius: 3px; padding: 19px 0 0 19px; }
  .entry time { display: inline-block; background: var(--stamp); padding: 2px 9px; font-size: 13px; color: #333; }
  .entry time small { color: var(--muted); font-size: 13px; }
  .entry p { margin-top: 8px; font-size: 15px; color: #444; }
</style>
</head>
<body>
  <aside class="sidebar">
    <div class="brand-bar">
      <span class="brand-name">Deskwell</span>
      <svg class="menu-toggle" viewBox="0 0 36 40"><polygon points="18,0 36,10 36,30 18,40 0,30 0,10" fill="#ece6f8"/><rect x="8" y="13" width="20" height="2.6" fill="#333"/><rect x="8" y="18.7" width="20" height="2.6" fill="#333"/><rect x="8" y="24.4" width="20" height="2.6" fill="#333"/></svg>
    </div>
    <div class="new-ticket">NEW TICKET <svg width="16" height="10" viewBox="0 0 16 10"><path d="M1 1l7 7 7-7" stroke="#fff" stroke-width="2.4" fill="none"/></svg></div>
    <ul class="nav">
      <li class="nav-item active"><svg class="nav-icon" viewBox="0 0 26 26" fill="none" stroke="#fff" stroke-width="1.4"><circle cx="13" cy="13" r="11"/><path d="M13 14l4-6M6 15h2M18 15h2M13 5v2"/><path d="M8 20h10"/></svg>DASHBOARD</li>
      <li class="nav-item"><svg class="nav-icon" viewBox="0 0 26 26" fill="none" stroke="#9a9ca6" stroke-width="1.4"><rect x="2" y="7" width="22" height="12" rx="2"/><path d="M6 7V4h14v3M6 19v3h14v-3"/></svg>TICKETS<svg class="nav-caret" width="16" height="10" viewBox="0 0 16 10"><path d="M1 1l7 7 7-7" stroke="#c9cbd3" stroke-width="1.8" fill="none"/></svg></li>
      <li class="nav-item"><svg class="nav-icon" viewBox="0 0 26 26" fill="none" stroke="#9a9ca6" stroke-width="1.4"><rect x="1" y="5" width="24" height="16"/><path d="M1 5l12 10 12-10M1 21l9-8M25 21l-9-8"/></svg>CONTACTS</li>
      <li class="nav-item"><svg class="nav-icon" viewBox="0 0 26 26" fill="none" stroke="#9a9ca6" stroke-width="1.4"><circle cx="13" cy="13" r="5"/><circle cx="13" cy="13" r="10" stroke-dasharray="4 2.5"/></svg>ADMIN SETTINGS<svg class="nav-caret" width="16" height="10" viewBox="0 0 16 10"><path d="M1 1l7 7 7-7" stroke="#c9cbd3" stroke-width="1.8" fill="none"/></svg></li>
      <li class="nav-item"><svg class="nav-icon" viewBox="0 0 26 26" fill="none" stroke="#9a9ca6" stroke-width="1.4"><rect x="1" y="6" width="22" height="15" rx="1"/><path d="M1 10h22M4 16h6M25 8v15H5"/></svg>ACCOUNT &amp; BILLING</li>
    </ul>
  </aside>

  <header class="topbar">
    <h1 class="page-title">Dasboard</h1>
    <div class="search">Search<svg width="20" height="20" viewBox="0 0 20 20" fill="none" stroke="#555" stroke-width="1.8"><circle cx="8" cy="8" r="6.5"/><path d="M13 13l6 6"/></svg></div>
    <div class="user-strip"></div>
    <svg class="avatar" width="46" height="52" viewBox="0 0 46 52"><defs><linearGradient id="av" x1="0" y1="0" x2="1" y2="1"><stop offset="0" stop-color="#8d5cd8"/><stop offset="1" stop-color="#4d2794"/></linearGradient></defs><polygon points="23,0 46,13 46,39 23,52 0,39 0,13" fill="url(#av)"/><text x="23" y="32" text-anchor="middle" font-family="Mulish, sans-serif" font-weight="700" font-size="18" fill="#fff">AK</text></svg>
    <svg class="kebab" width="6" height="20" viewBox="0 0 6 20" fill="#888"><circle cx="3" cy="3" r="2.3"/><circle cx="3" cy="10" r="2.3"/><circle cx="3" cy="17" r="2.3"/></svg>
  </header>

  <p class="greeting">Good Morning, <span>Adrian</span></p>

  <section class="stats">
    <div class="stat primary"><svg viewBox="0 0 129 151"><polygon points="64.5,1 128,38 128,113 64.5,150 1,113 1,38" fill="#fff"/></svg><div class="stat-value">16</div><div class="stat-label">Open Tickets</div></div>
    <div class="stat"><svg viewBox="0 0 129 151"><polygon points="64.5,1 128,38 128,113 64.5,150 1,113 1,38" fill="#fff"/></svg><div class="stat-value">14</div><div class="stat-label">Due Today</div></div>
    <div class="stat"><svg viewBox="0 0 129 151"><polygon points="64.5,1 128,38 128,113 64.5,150 1,113 1,38" fill="#fff"/></svg><div class="stat-value">14</div><div class="stat-label">Unassiggned</div></div>
    <div class="stat zero"><svg viewBox="0 0 129 151"><polygon points="64.5,1 128,38 128,113 64.5,150 1,113 1,38" fill="#fff"/></svg><div class="stat-value">0</div><div class="stat-label">Over Due</div></div>
    <div class="stat zero"><svg viewBox="0 0 129 151"><polygon points="64.5,1 128,38 128,113 64.5,150 1,113 1,38" fill="#fff"/></svg><div class="stat-value">0</div><div class="stat-label">On Hold</div></div>
    <div class="stat"><svg viewBox="0 0 129 151"><polygon points="64.5,1 128,38 128,113 64.5,150 1,113 1,38" fill="#fff"/></svg><div class="stat-value">11</div><div class="stat-label">Not Resolved</div></div>
  </section>

  <section class="activity">
    <h2 class="activity-head">Recent Activities</h2>
    <div class="day-tag" style="top:67px">TODAY</div>
    <div class="entry" style="top:104px"><time>4:49 <small>pm</small></time><p>Marcus Hale assigned forgot to cc, trying again (#15) to Marcus Hale.</p></div>
    <div class="entry" style="top:197px"><time>10:49 <small>am</small></time><p>Marcus Hale assigned forgot to cc, trying again (#15) to Marcus Hale.</p></div>
    <div class="entry" style="top:291px"><time>9:49 <small>am</small></time><p>Marcus Hale added a note to the ticket Test From Email (#12)</p></div>
    <div class="day-tag" style="top:393px">YESTERDAY</div>
    <div class="entry" style="top:429px"><time>5:49 <small>pm</small></time><p>Marcus Hale assigned test (#15)</p></div>
    <div class="entry" style="top:522px"><time>12:00 <small>pm</small></time><p>Lina Ortez raised a new ticket test (#16)</p></div>
  </section>
</body>
</html>
```